Valbrina Soletti Winery 2023 Label

We are just about to bottle our very first Napa Valley Cabernet Sauvignon and need label ideas

Target Market(s)

Cab drinkers who like Napa California Cabs

Industry/Entity Type

Wine Making

Logo Text

Valbrina Soletti 2023 Napa Estate Grown Cabernet Sauvignon

Requirements
Must have
• Winery Name, year of vintage and Napa Estate Cab
Nice to have
• If using the initials V and S use gold letters on black or red background

```html
<!DOCTYPE html>
<html lang="en">
<head>
<meta charset="UTF-8">
<title>Valbrina Soletti Vineyards – 2023 Cabernet Sauvignon Label</title>
<link href="https://fonts.googleapis.com/css2?family=EB+Garamond:wght@400;500&display=swap" rel="stylesheet">
<style>
  :root {
    --backdrop: #e6e5e6;
    --label-red: #c42228;
    --label-white: #f4f4f3;
    --ink-dark: #1c1a1a;
    --ink-light: #ffffff;
    --edge-shadow: rgba(0, 0, 0, 0.12);
  }
  * { margin: 0; padding: 0; box-sizing: border-box; }
  html, body {
    width: 1200px;
    height: 900px;
    overflow: hidden;
    background: var(--backdrop);
  }
  .canvas {
    width: 1200px;
    height: 900px;
    display: flex;
    align-items: center;
    justify-content: center;
  }
  .wine-label {
    width: 520px;
    height: 760px;
    display: flex;
    flex-direction: column;
    box-shadow: 0 10px 30px var(--edge-shadow);
    font-family: 'EB Garamond', Georgia, serif;
  }
  .label-crest {
    flex: 0 0 54%;
    background: var(--label-red);
    display: flex;
    align-items: flex-end;
    justify-content: center;
    padding-bottom: 48px;
  }
  .winery-mark {
    display: inline-flex;
    flex-direction: column;
    align-items: flex-end;
    color: var(--ink-light);
  }
  .winery-name {
    font-size: 46px;
    font-weight: 400;
    letter-spacing: 0.5px;
    line-height: 1.05;
  }
  .winery-sub {
    font-size: 30px;
    font-weight: 400;
    line-height: 1.1;
    margin-right: 4px;
  }
  .label-varietal {
    flex: 1;
    background: var(--label-white);
    display: flex;
    flex-direction: column;
    align-items: center;
    justify-content: center;
    color: var(--ink-dark);
  }
  .varietal-block {
    display: inline-flex;
    flex-direction: column;
    align-items: flex-end;
  }
  .varietal-name {
    font-size: 38px;
    font-weight: 400;
    line-height: 1.05;
  }
  .varietal-origin {
    font-size: 19px;
    line-height: 1.2;
    margin-right: 18px;
  }
  .vintage-year {
    margin-top: 40px;
    font-size: 52px;
    font-weight: 400;
    letter-spacing: 1px;
  }
</style>
</head>
<body>
  <main class="canvas">
    <section class="wine-label" aria-label="Valbrina Soletti Vineyards wine label">
      <div class="label-crest">
        <div class="winery-mark">
          <span class="winery-name">Valbrina Soletti</span>
          <span class="winery-sub">Vineyards</span>
        </div>
      </div>
      <div class="label-varietal">
        <div class="varietal-block">
          <span class="varietal-name">Cabernet Sauvignon</span>
          <span class="varietal-origin">Napa Estate Grown</span>
        </div>
        <span class="vintage-year">2023</span>
      </div>
    </section>
  </main>
</body>
</html>
```